Winter of the Lantern Summer Production

I am looking for a one sided A5 vehicle flyer for my Musical Theatre Summer Course 'Winter of The Lantern. It needs to look professional , but appealing to children and eye-catching.

I attach our company logo's below

Details:

We are searching for Budding Young Stars to perform in our dazzling youth production of 'Winter of The Lantern'.All roles are available!

Ages 4-18 years ( Grouped according to age)

Beginners - advanced welcome

Monday 7th August - Friday 11th August 2017 @ The Harbour Hall Kestby, 218 Marrowdale Rd SE4 7QT
10am - 2pm each day
£100 for the week ( based on the affordable fee of £5 per hour)

Fully costumed production at the end of the week with a role for everyone in the fantastic theatre space at The Harbour, in New Eltham.There will be the opportunity to purchase a DVD of your performance.

The week will be taught by our qualified industry experts and will include drama, singing and dance as well as make-up, confidence building drama games, audition opportunities and advice, competitions, prizes and much much more!

Bright Lane Stage are an accredited multi-award winning theatre company, who pride themselves on offering youngsters the opportunity to take part in local performances at affordable prices. They have been offering their sell out summer courses for over 15 years.

Please visit www.brightlanestage-example.co.uk or call 020 7946 0718 or fill out the form below and return to : Bright Lane Stage Ltd. PO Box 47209, London SE4 2RW or drop into one of our centres ( details on our website:

Name........................................................................................

DOB..........................................................................................

Email address ( Bock capitals please) .....................................................................................................

Phone number ,.............................................................................

Medical conditions.......................................................................

How you heard about us

..................................................................................................

www.brightlanestage-example.co.uk 020 7946 0719

Target Market(s)

Children and young people ages 4-18yrs - boys as well as girls

Industry/Entity Type

Performing Art

Font styles to use
Decorative

Colors
6b449b
d3a5cc
eea4c8
fbee3e
fece3e

Requirements
Must have
• Company logo
• website www..brightlanestage-example.co.uk
• fb page www.facebook.com/Brightlanestagetheatre/
• phone number 020 79460719
• Emphasis on AFFORDABLE
• A few pictures that look like Winter of the lantern
• A booking form ( detailed above) at the bottom
• BELOW IS A LEAFLET FROM ANOTHER COMPANY WHICH I LIKE

```html
<!DOCTYPE html>
<html lang="en">
<head>
<meta charset="utf-8">
<title>Winter of the Lantern – Youth Summer Production</title>
<link rel="stylesheet" href="https://fonts.googleapis.com/css2?family=Bebas+Neue&family=Archivo+Black&family=Kalam:wght@400;700&family=Kaushan+Script&family=EB+Garamond:ital,wght@0,400;0,700;1,700&display=swap">
<style>
  :root {
    --purple: #6b449b;
    --pink: #eaa3c9;
    --lilac: #d3a5cc;
    --yellow: #fbee3e;
    --gold: #fece3e;
    --red: #e8322f;
    --ink: #111111;
    --paper: #ffffff;
  }
  * { box-sizing: border-box; margin: 0; padding: 0; }
  html, body { width: 1200px; height: 846px; overflow: hidden; background: var(--paper); }
  .flyer { position: relative; width: 1200px; height: 846px; background: var(--paper); font-family: "EB Garamond", Georgia, serif; color: var(--ink); }

  .header { position: absolute; left: 20px; top: 14px; width: 1165px; height: 124px; background: var(--pink); text-align: center; }
  .header__kicker { font-family: "Bebas Neue", Impact, sans-serif; font-size: 39px; line-height: 1; color: #fff; padding-top: 18px; }
  .header__kicker strong { color: var(--ink); font-weight: 400; }
  .header__title { font-family: "Bebas Neue", Impact, sans-serif; font-size: 68px; line-height: 1; color: var(--purple); margin-top: 1px; }
  .header__title em { font-style: normal; color: var(--red); }

  .tag { position: absolute; top: 142px; height: 74px; background: var(--purple); color: #fff; text-align: center; font-family: "Kalam", cursive; font-weight: 700; }
  .tag--roles { left: 32px; width: 202px; font-size: 29px; line-height: 31px; padding-top: 6px; }
  .tag--ages { left: 243px; width: 225px; font-size: 31px; line-height: 38px; padding-top: 4px; }
  .tag--ages small { display: block; font-family: "EB Garamond", Georgia, serif; font-weight: 400; font-size: 16px; line-height: 18px; }

  .artwork { position: absolute; left: 20px; top: 222px; width: 450px; height: 460px; }
  .burst-text { position: absolute; left: 272px; top: 306px; width: 136px; text-align: center; font-family: "Kalam", cursive; font-weight: 700; font-size: 27px; line-height: 34px; color: #fff; transform: rotate(-4deg); }

  .venue { position: absolute; left: 40px; top: 560px; width: 230px; color: #fff; }
  .venue__label { font-family: "Bebas Neue", Impact, sans-serif; font-size: 26px; line-height: 1; letter-spacing: 1px; }
  .venue__name { font-family: "Kalam", cursive; font-weight: 700; font-size: 22px; line-height: 26px; margin-top: 4px; }
  .venue__address { font-size: 17px; line-height: 21px; }

  .badge { position: absolute; }
  .badge--listing { left: 20px; top: 682px; width: 158px; height: 140px; background: #f4f6ee; border-top: 3px solid #e8edd9; }
  .badge--school { left: 198px; top: 702px; width: 264px; height: 100px; background: #eeeeee; border: 1px solid #d6d6d6; }

  .details { position: absolute; left: 478px; top: 146px; width: 700px; }
  .details__dates { font-family: "Bebas Neue", Impact, sans-serif; font-size: 46px; line-height: 1; color: var(--ink); }
  .details__dates sup { font-size: 22px; vertical-align: 20px; }
  .details__hours { font-family: "Archivo Black", Arial, sans-serif; font-size: 38px; line-height: 1; color: var(--purple); margin-top: 4px; letter-spacing: 1px; }
  .details__price { margin-top: 14px; font-size: 17px; }
  .script { font-family: "Kaushan Script", cursive; font-size: 24px; color: var(--purple); }
  .script--red { color: var(--red); }

  .brand { position: absolute; left: 1000px; top: 240px; width: 170px; display: flex; align-items: center; gap: 8px; }
  .brand__dot { width: 26px; height: 26px; border-radius: 50%; background: var(--gold); flex: none; }
  .brand__name { font-family: "EB Garamond", Georgia, serif; font-weight: 700; font-size: 22px; line-height: 1.05; color: var(--red); }

  .copy { position: absolute; left: 478px; width: 700px; font-size: 17px; line-height: 21px; }
  .copy--production { top: 300px; width: 520px; }
  .copy--course { top: 354px; }
  .copy--company { top: 430px; }
  .copy--contact { top: 506px; }
  .copy b { font-weight: 700; }
  .highlight { font-style: italic; font-weight: 700; color: var(--purple); font-size: 21px; }
  .purple { color: var(--purple); }

  .form { position: absolute; left: 478px; top: 604px; width: 670px; font-size: 17px; }
  .form__row { display: flex; align-items: baseline; height: 31px; }
  .form__line { flex: 1; border-bottom: 1.5px dotted #333; margin: 0 6px 0 4px; height: 14px; }
  .form__line--name { flex: 3; }

  .footer { position: absolute; left: 478px; top: 768px; width: 707px; height: 62px; background: var(--gold); display: flex; align-items: center; justify-content: center; gap: 12px; font-family: "Bebas Neue", Impact, sans-serif; font-size: 40px; line-height: 1; }
  .footer__site { color: var(--ink); }
  .footer__phone { color: var(--purple); }
</style>
</head>
<body>
<main class="flyer">
  <header class="header">
    <p class="header__kicker">We are <strong>searching for budding young stars</strong> to perform in our dazzling</p>
    <h1 class="header__title">Youth production of <em>‘Winter of the Lantern’</em></h1>
  </header>

  <div class="tag tag--roles">All roles<br>are available!</div>
  <div class="tag tag--ages">Ages 4–18 yrs<small>(Grouped according to age)</small></div>

  <svg class="artwork" viewBox="0 0 450 460" role="img" aria-label="Illustration of two winter story characters in white silhouette sharing a glowing lantern, over a purple to yellow glow">
    <defs>
      <linearGradient id="glow" x1="0" y1="0" x2="1" y2="0">
        <stop offset="0" stop-color="#6b449b"/>
        <stop offset="0.5" stop-color="#b99a9c"/>
        <stop offset="1" stop-color="#fbee3e"/>
      </linearGradient>
    </defs>
    <polygon points="0,0 330,0 450,110 450,375 370,460 0,460" fill="url(#glow)"/>
    <polygon fill="#e8322f" points="320,50 334,78 355,58 358,88 388,78 378,106 408,112 384,130 408,150 378,156 388,184 358,174 355,204 334,184 320,212 306,184 285,204 282,174 252,184 262,156 232,150 256,130 232,112 262,106 252,78 282,88 285,58 306,78"/>
  </svg>
  <div class="burst-text">Light the<br>Lantern!</div>

  <div class="venue">
    <p class="venue__label">Venue</p>
    <p class="venue__name">The Harbour Hall Kestby</p>
    <p class="venue__address">218 Marrowdale Rd SE4 7QT</p>
  </div>

  <div class="badge badge--listing" role="img" aria-label="Listing badge"></div>
  <div class="badge badge--school" role="img" aria-label="Recognised school badge"></div>

  <section class="details">
    <p class="details__dates">Monday 7<sup>th</sup> August - Friday 11<sup>th</sup> August 2017</p>
    <p class="details__hours">10AM - 2PM EACH DAY</p>
    <p class="details__price"><span class="script">£100 for the week</span> (based on the <span class="script script--red">affordable fee</span> of £5 per hour)</p>
  </section>

  <div class="brand"><span class="brand__dot"></span><span class="brand__name">Bright Lane Stage</span></div>

  <p class="copy copy--production">Fully costumed production at the end of the week with a role for everyone. There will be the opportunity to purchase a DVD of your performance.</p>
  <p class="copy copy--course">The week will be taught by our <span class="highlight">qualified industry experts</span> and will include drama, singing and dance as well as make-up, confidence building drama games, audition opportunities and advice, competitions, prizes and much much more!</p>
  <p class="copy copy--company">Bright Lane Stage are an accredited <span class="highlight">multi-award winning</span> theatre company, who pride themselves on offering youngsters the opportunity to take part in local performances at affordable prices. They have been offering their sell out summer courses for over 15 years.</p>
  <p class="copy copy--contact">Please visit <b>www.brightlanestage-example.co.uk</b> or call <b>020 7946 0718</b> or fill out the <b>form below</b> and return to: <b class="purple">Bright Lane Stage Ltd. PO Box 47209, London SE4 2RW</b> or drop into one of our centres <span class="purple">(details on our website)</span>. Find us at <b>www.facebook.com/Brightlanestagetheatre/</b></p>

  <form class="form">
    <div class="form__row">Name<span class="form__line form__line--name"></span>DOB<span class="form__line"></span></div>
    <div class="form__row">Email address (Block capitals please)<span class="form__line"></span></div>
    <div class="form__row">Phone number ,<span class="form__line"></span></div>
    <div class="form__row">Medical conditions<span class="form__line"></span></div>
    <div class="form__row">How you heard about us<span class="form__line"></span></div>
  </form>

  <footer class="footer">
    <span class="footer__site">WWW.BRIGHTLANESTAGE-EXAMPLE.CO.UK</span>
    <span class="footer__phone">020 7946 0719</span>
  </footer>
</main>
</body>
</html>
```